Letterhead Design Project

I need a letterhead design that is simple, modern, and colorful.

We publish novels that speak to female empowerment. With our fiction, we hope to encourage women to live boldly and love themselves without apology.

Our logo is red and teal so I'd like to see those colors continued in the letterhead.

The final design should be bold and inspiring.
Updates

Hello talented designers!

We will also be needing a business card design which will hopefully go to the designer of our letterhead. Please keep that in mind.

Thanks for all your efforts (in advance)!

I'd like the following information included:

Address - 4178 North Fallowmere Street, Suite #207, Chicago Ridge, Illinois 60415
Website - www.quillhavenpress.example
Email - info@quillhavenpress.example

Please see the updated files. The part of the logo that was red is now pink. And I've uploaded .eps and .ai formats. Thanks.

Target Market(s)

women, age 25+, college educated professionals

Requirements
Nice to have
• swirls or flourishes
Should not have
• dots or stripes

```html
<!DOCTYPE html>
<html lang="en">
<head>
<meta charset="utf-8">
<title>Quillhaven Press Letterhead</title>
<link rel="stylesheet" href="https://fonts.googleapis.com/css2?family=EB+Garamond:wght@400;500;700&display=swap">
<style>
  :root {
    --paper: #ffffff;
    --ink: #1c1c1c;
    --brand-red: #8d1c22;
    --accent-red: #d8232a;
    --deep-red: #7a1116;
    --teal: #245a72;
    --mark-pink: #c8304a;
    --mark-teal: #5fb6c4;
    --signature-tone: #e4e4e4;
  }
  * { margin: 0; padding: 0; box-sizing: border-box; }
  html, body { width: 849px; height: 1200px; overflow: hidden; background: var(--paper); }
  .letterhead {
    position: relative;
    width: 849px;
    height: 1200px;
    background: var(--paper);
    font-family: "EB Garamond", Georgia, serif;
    color: var(--ink);
    overflow: hidden;
  }
  .brand {
    position: absolute;
    top: 30px;
    left: 0;
    width: 100%;
    text-align: center;
  }
  .brand-symbol {
    display: block;
    width: 16px;
    height: 16px;
    margin: 0 auto 150px;
    visibility: hidden;
  }
  .brand-name {
    margin-top: 22px;
    font-size: 32px;
    font-weight: 500;
    line-height: 1;
    color: var(--brand-red);
  }
  .letter {
    position: absolute;
    top: 328px;
    left: 128px;
    width: 600px;
  }
  .letter-title {
    font-size: 17px;
    font-weight: 700;
    letter-spacing: 0.2px;
    line-height: 22px;
    margin-bottom: 27px;
  }
  .letter p {
    font-size: 17.6px;
    line-height: 24px;
    margin-bottom: 10px;
    hyphens: manual;
  }
  .signature {
    position: absolute;
    left: 130px;
    top: 915px;
    width: 195px;
    height: 175px;
    border-radius: 50% 40% 50% 45%;
    background: radial-gradient(ellipse at center, var(--signature-tone) 0%, rgba(228,228,228,0) 75%);
  }
  .footer-swoosh {
    position: absolute;
    left: 0;
    bottom: 0;
    width: 849px;
    height: 340px;
  }
</style>
</head>
<body>
<main class="letterhead">
  <header class="brand">
    <div class="brand-symbol" aria-hidden="true"></div>
    <div class="brand-name">Quillhaven Press</div>
  </header>

  <article class="letter">
    <h1 class="letter-title">LETTERHEAD DESIGN FOR QUILLHAVEN PRESS</h1>
    <p>Nonsenist ulluptate peritasit as quam, essin este nem. Illorro con nis ea natiam facea nossintus. Equi accae mo et occus cum iumqui aliquamet, si dolorrumqui dolupicil ipsum quatusdae autaspe digenem et, offic to te et aut ipsus milit, il is dolorum faci diatem res unt omnis aliquo minctis unturit volorro dolut volori&shy;busam intiore volupta tissimped es vollandi odite pos delest, con nos destius ducid quis et quas aboratenit omnis in nempore volupta imporer untias rem inctota turiandae.</p>
    <p>Inis de por rem quatemporunt fugia quam faceatios sinciuscit aboria cuptur sus aliaestrum reperum dent est atur amusa veligent volorecta cus quibus ditatis exeruntur, eseri assitatenest quam rest volorio resequam eos conestiae endae vide volores sumquae cabori bea qui sero expedic iaectaquam quissit aestiundit officiis pro volorum abor magnisci denditi volorro beariostiste escia corias dolupta com&shy;nit omnim eumquia tendelesciam labor ra dolluptiundi ut lantorehent evel eum rem qui am nonsedi ationsectia corum harum repudam faccull anderum fugitas volupitas.</p>
    <p>Nimostia evellendia aut aut etum que peri ate paruptur atur autem quo mi, ip&shy;suntus nos ipsa dit everio et ut as rem fuga. Mus et, sum sequoditium sum utendi&shy;aspid millam, aut volupta tincid ut ut quo ducim fugitat estinum delest harumque nonsequibus volut eatempore, cuptam harion pra eatum qui nos possit res aut volorersped que nos minient rae cum re de officil iquunti.</p>
  </article>

  <div class="signature" role="img" aria-label="Handwritten signature of the sender"></div>

  <svg class="footer-swoosh" viewBox="0 0 849 340" aria-hidden="true">
    <defs>
      <linearGradient id="bandRed" x1="0" y1="0" x2="0" y2="1">
        <stop offset="0" stop-color="var(--accent-red)"/>
        <stop offset="1" stop-color="var(--deep-red)"/>
      </linearGradient>
    </defs>
    <path d="M0,300 C300,275 600,190 849,28 L849,55 C600,210 300,292 0,318 Z" fill="url(#bandRed)"/>
    <path d="M0,316 C300,290 600,208 849,53 L849,340 L0,340 Z" fill="var(--teal)"/>
    <path d="M0,318 C180,322 380,330 560,340 L0,340 Z" fill="var(--paper)"/>
    <path d="M0,326 C180,330 380,336 520,340 L560,340 C380,330 180,322 0,318 Z" fill="var(--accent-red)"/>
  </svg>
</main>
</body>
</html>
```